Label for a bottle of Gin soon to launch in the UK.

We need a label for a gin called Halworth Gin. It is very important that the label does not infringe any copyrights of the football club so please avoid the colour blue or anything related to football or the club. The example bottle below shows the bottle that we will be using. The gin will be clear not pink, the use of gold on the label is encouraged.
Should not infringe on the brand shown in the example image.

Club

Sans Serif

• Here is a link to the bottle that the label must fit onto https://www.flaskcrate-depot.co.uk/Glass-bottles/Glass-bottles/700ml-glass-bottles/700ml-clear-glass-bottle-Marosa.html
• No use of blue or anything related to football or Halworth Football Club or Moorhawks. Avoid Red also. White, gold and black should be primary colours used

```html
<!DOCTYPE html>
<html lang="en">
<head>
<meta charset="utf-8">
<title>Halworth Gin – Bottle Label</title>
<link rel="stylesheet" href="https://fonts.googleapis.com/css2?family=Archivo:wght@600;700&family=Bebas+Neue&family=Libre+Baskerville:wght@700&family=Oswald:wght@300&family=Yellowtail&display=swap">
<style>
  :root {
    --backdrop: #232323;
    --paper: #dfe6dc;
    --paper-shade: #d3dcd1;
    --ink: #2e2b3b;
    --gold: #a88a4e;
    --gold-light: #d2bd88;
    --wine: #8c2b4d;
    --wine-soft: #d6b3bf;
    --rule: #9aa39a;
  }
  * { box-sizing: border-box; margin: 0; padding: 0; }
  html, body {
    width: 1200px; height: 1200px; overflow: hidden;
    background: var(--backdrop);
  }
  .label {
    position: absolute;
    left: 186px; top: 224px;
    width: 829px; height: 742px;
    background: radial-gradient(ellipse at 30% 30%, var(--paper) 0%, var(--paper-shade) 100%);
    box-shadow: 0 18px 40px rgba(0,0,0,.45);
  }
  .label::before, .label::after {
    content: "";
    position: absolute; left: 0; right: 0; height: 8px;
    background-size: 28px 8px;
    background-repeat: repeat-x;
  }
  .label::before {
    top: 0;
    background-image: radial-gradient(circle at 50% 0, var(--backdrop) 7px, transparent 7.5px);
  }
  .label::after {
    bottom: 0;
    background-image: radial-gradient(circle at 50% 100%, var(--backdrop) 7px, transparent 7.5px);
  }
  .label-art { position: absolute; inset: 0; }
  .distillery { font-family: "Libre Baskerville", serif; font-weight: 700; font-size: 22px; letter-spacing: 4px; fill: var(--ink); }
  .brand-name { font-family: "Bebas Neue", sans-serif; font-size: 178px; letter-spacing: 4px; fill: var(--ink); stroke: var(--gold); stroke-width: 3px; paint-order: stroke; }
  .product { font-family: "Bebas Neue", sans-serif; font-size: 300px; letter-spacing: 8px; fill: var(--ink); }
  .tagline { font-family: "Archivo", sans-serif; font-weight: 700; font-size: 15px; letter-spacing: 3px; fill: var(--ink); }
  .origin { font-family: "Archivo", sans-serif; font-weight: 600; font-size: 28px; letter-spacing: 4px; fill: url(#goldFoil); }
  .field-label { font-family: "Archivo", sans-serif; font-weight: 700; font-size: 9px; letter-spacing: 1px; fill: var(--ink); }
  .field-value { font-family: "Oswald", sans-serif; font-weight: 300; font-size: 22px; fill: var(--ink); }
  .motto { font-family: "Yellowtail", cursive; font-size: 46px; fill: var(--wine); }
  .rule { stroke: var(--rule); stroke-width: 1; stroke-dasharray: 2 3; }
  .divider { stroke: var(--rule); stroke-width: 1; }
  .seal-ring { fill: none; stroke: url(#goldFoil); stroke-width: 3; }
  .seal-name { font-family: "Archivo", sans-serif; font-weight: 700; font-size: 17px; letter-spacing: 2px; fill: var(--gold); }
</style>
</head>
<body>
<div class="label">
  <svg class="label-art" width="829" height="742" viewBox="0 0 829 742" xmlns="http://www.w3.org/2000/svg">
    <defs>
      <linearGradient id="goldFoil" x1="0" y1="0" x2="1" y2="1">
        <stop offset="0" stop-color="#8a6d36"/>
        <stop offset="0.45" stop-color="#d2bd88"/>
        <stop offset="1" stop-color="#7d6330"/>
      </linearGradient>
      <path id="arcDistillery" d="M 200 100 Q 414 78 628 100"/>
      <path id="arcBrand" d="M 70 280 Q 414 215 758 280"/>
      <path id="arcOrigin" d="M 230 550 Q 414 528 598 550"/>
    </defs>

    <text class="distillery"><textPath href="#arcDistillery" startOffset="50%" text-anchor="middle">NONAME DISTILLERY</textPath></text>

    <text class="brand-name"><textPath href="#arcBrand" startOffset="50%" text-anchor="middle">HALWORTH</textPath></text>

    <text class="product" x="414" y="456" text-anchor="middle">GIN</text>

    <rect x="42" y="444" width="196" height="252" fill="var(--wine-soft)" opacity="0.7" role="img" aria-label="Engraved illustration of a gentleman in a top hat under an umbrella in the rain, standing beside a monogrammed barrel"/>

    <text class="tagline" x="414" y="514" text-anchor="middle">8 FINE BOTANICALS</text>
    <text class="origin"><textPath href="#arcOrigin" startOffset="50%" text-anchor="middle">LONDON, ENGLAND</textPath></text>
    <text class="tagline" x="414" y="578" text-anchor="middle">CAREFULLY BLENDED</text>

    <line class="rule" x1="150" y1="598" x2="614" y2="598"/>
    <line class="rule" x1="150" y1="648" x2="614" y2="648"/>

    <text x="150" y="636"><tspan class="field-label">BATCH#</tspan><tspan class="field-value" dx="6">0003</tspan></text>
    <text class="motto" x="400" y="640" text-anchor="middle">Bad luck gin</text>
    <text x="556" y="636"><tspan class="field-label">BOTTLE#</tspan><tspan class="field-value" dx="6">0422</tspan></text>

    <text class="field-label" x="240" y="672">DISTILLER</text>
    <rect x="240" y="650" width="66" height="42" fill="var(--wine-soft)" opacity="0.5" role="img" aria-label="Handwritten distiller signature"/>
    <line class="divider" x1="312" y1="660" x2="312" y2="700"/>
    <text x="318" y="690"><tspan class="field-label" dy="-16">ALCOHOL</tspan><tspan class="field-value" dx="8" dy="16">40%VOL</tspan></text>
    <line class="divider" x1="472" y1="660" x2="472" y2="700"/>
    <text x="480" y="690"><tspan class="field-label" dy="-16">VOLUMEN</tspan><tspan class="field-value" dx="12" dy="16">70 CL</tspan></text>

    <circle class="seal-ring" cx="692" cy="584" r="100"/>
    <text class="seal-name" x="692" y="578" text-anchor="middle">HALWORTH<tspan x="692" dy="22">GIN COMPANY</tspan></text>
  </svg>
</div>
</body>
</html>
```